Stationery Design Project

Would like to have the design elements we created in for our website (www.brook-holdings.example), incorporated in a stationery design layout.
Updates
Colors used in the logo attachments do not need to be used. We are open to different color variations. Looking for a crisp, clean, modern update using the design elements in attachments and which can also be viewed on or website.
A note to designers:
Project Deadline Extended
Reason: Due to update in our project description and requirements, we have decided to extend the deadline of this project to provide ample opportunity to all designers participating .
Requirements
Must have
- Must have continuity with the theme and design features used in our website. Have attached .jpg images of some of the design elements.

```html
<!DOCTYPE html>
<html lang="en">
<head>
<meta charset="utf-8">
<title>Brook Holdings Inc — Letterhead</title>
<link rel="stylesheet" href="https://fonts.googleapis.com/css2?family=Open+Sans:wght@300;400&family=Arimo:wght@400&display=swap">
<style>
  :root {
    --brand-blue: #1a7dc0;
    --brand-green: #57b045;
    --rule-grey: #999999;
    --text-grey: #6f6f6f;
    --ghost-grey: #ececec;
    --page-edge: #e6e6e6;
    --paper: #ffffff;
  }
  * { margin: 0; padding: 0; box-sizing: border-box; }
  html, body {
    width: 900px;
    height: 1200px;
    overflow: hidden;
    background: var(--paper);
  }
  .letterhead {
    position: relative;
    width: 900px;
    height: 1200px;
    background: var(--paper);
    font-family: "Arimo", Arial, sans-serif;
  }
  .page-edge {
    position: absolute;
    left: 19px; top: 25px;
    width: 862px; height: 1148px;
    border: 1px solid var(--page-edge);
  }
  .brand-name {
    position: absolute;
    left: 66px; top: 70px;
    font-family: "Open Sans", sans-serif;
    font-weight: 400;
    font-size: 37px;
    letter-spacing: -0.5px;
    color: var(--brand-blue);
    white-space: nowrap;
  }
  .header-band {
    position: absolute;
    left: 408px; top: 76px;
    width: 473px; height: 44px;
    background: var(--brand-green);
  }
  .side-name {
    position: absolute;
    left: 815px; top: 415px;
    transform: translate(-50%, -50%) rotate(-90deg);
    font-family: "Open Sans", sans-serif;
    font-weight: 300;
    font-size: 82px;
    color: var(--ghost-grey);
    white-space: nowrap;
  }
  .footer-title {
    position: absolute;
    left: 0; top: 1061px;
    width: 915px;
    text-align: center;
    font-size: 15px;
    color: var(--brand-blue);
  }
  .contact-column {
    position: absolute;
    top: 1098px;
    width: 204px;
    text-align: center;
    font-size: 13px;
    line-height: 20px;
  }
  .contact-column--address { left: 139px; color: var(--text-grey); }
  .contact-column--phone { left: 348px; color: var(--brand-green); }
  .contact-column--web { left: 557px; color: var(--text-grey); }
  .contact-column::after {
    content: "";
    position: absolute;
    left: 0; top: 45px;
    width: 204px; height: 4px;
    background: var(--brand-green);
  }
  .contact-column--phone::after { background: var(--rule-grey); }
</style>
</head>
<body>
  <main class="letterhead">
    <div class="page-edge"></div>
    <div class="brand-name">Brook Holdings Inc</div>
    <div class="header-band"></div>
    <div class="side-name" aria-hidden="true">Brook Holdings</div>

    <footer>
      <p class="footer-title">Brook Holdings, Inc.</p>
      <div class="contact-column contact-column--address">
        418-Alder Creek Road Suite 12,<br>Millbrook, GA - 30999,
      </div>
      <div class="contact-column contact-column--phone">
        Phone : (555) 014-2287<br>Fax : (555) 014-2290
      </div>
      <div class="contact-column contact-column--web">
        info@brook-holdings.example<br>www.brook-holdings.example
      </div>
    </footer>
  </main>
</body>
</html>
```